Tri-fold Brochure Design for New Custom Home Model

We need an expert to design a tri-fold brochure to showcase our new custom home model.<br/>The concept is as follow:<br/>We are introducing a fixed prize affordable custom home. We are trying to target landowners or homeowners who would like to build a custom home. We have a fixed design for exterior, interior. 3 level layout. Basement, main level, first floor.<br/>We have hand-drew the desired layout as you can see in the document attached names "hand-drawing". We would like the design to follow that idea.<br/>The required photos and info are attached. Please check out the attached documents here.<br/> The text content, material details can be found in the PDF file attached.

Target Market(s)

Home Owner, Land-owner, people who wants to build a new home

Industry/Entity Type

Residential Construction

Font styles to use
Sans Serif

Colors
ec1f27
fffefd

Requirements
Must have
• Formal text language, attractive design
Nice to have
• Most attractive and lead generating design
Should not have
• more than two colours, flashy design.

```html
<!DOCTYPE html>
<html lang="en">
<head>
<meta charset="utf-8">
<title>Northshore Build Co. – Custom Home Brochure</title>
<link rel="stylesheet" href="https://fonts.googleapis.com/css2?family=Open+Sans:wght@300;400;700;800&family=Arimo:wght@700&display=swap">
<style>
  :root {
    --brand-red: #ec1f27;
    --brand-red-dark: #c5161d;
    --paper: #fffefd;
    --backdrop: #d9d4d3;
    --ink: #1a1a1a;
    --box-line: #b5b5b5;
  }
  * { box-sizing: border-box; margin: 0; padding: 0; }
  html, body { width: 1200px; height: 1200px; overflow: hidden; background: var(--backdrop); }
  .canvas { position: relative; width: 1000px; height: 1000px; transform: scale(1.2); transform-origin: 0 0; font-family: "Open Sans", sans-serif; }
  .abs { position: absolute; }

  /* Outer spread */
  .outer { left: 207px; top: 60px; width: 585px; height: 409px; background: var(--paper); }
  .kitchen-photo {
    left: 0; top: 0; width: 195px; height: 409px;
    background:
      linear-gradient(180deg, rgba(0,0,0,0) 0%, rgba(0,0,0,0) 55%, rgba(90,60,40,.0) 56%),
      linear-gradient(180deg, #eceae6 0%, #dedbd6 17%, #6a6f86 20%, #c98f68 38%, #b7b3ad 48%, #e9e8e5 55%, #e3e1dd 62%, #8a6a54 70%, #6d5242 80%, #c7c4bf 90%, #d6d3cf 100%);
  }
  .red-top { left: 195px; top: 0; width: 390px; height: 148px; background: var(--brand-red); }
  .red-side { left: 568px; top: 205px; width: 17px; height: 75px; background: var(--brand-red); }
  .red-foot-left { left: 195px; top: 330px; width: 210px; height: 63px; background: var(--brand-red); }
  .red-foot { left: 195px; top: 393px; width: 390px; height: 16px; background: var(--brand-red); border-top: 1px solid var(--brand-red-dark); }

  .why-title { left: 264px; top: 66px; color: var(--paper); font-weight: 800; font-size: 12px; letter-spacing: .2px; }
  .why-box { width: 47px; height: 47px; background: var(--paper); border: 1px solid var(--box-line); display: flex; align-items: center; justify-content: center; }
  .why-icon { width: 24px; height: 24px; fill: none; stroke: var(--brand-red); stroke-width: 2; stroke-linecap: round; stroke-linejoin: round; }

  .brand { display: flex; align-items: center; gap: 6px; color: var(--paper); }
  .brand-mark { border: 2.5px solid var(--paper); border-radius: 50%; flex: none; }
  .brand-name { font-weight: 400; line-height: 1.15; }
  .brand-top { left: 425px; top: 27px; }
  .brand-top .brand-mark { width: 40px; height: 40px; border-width: 4px; }
  .brand-top .brand-name { font-size: 11px; }
  .brand-foot { left: 272px; top: 360px; }
  .brand-foot .brand-mark { width: 18px; height: 18px; border-width: 2px; }
  .brand-foot .brand-name { font-size: 6px; }

  .house-frame { left: 405px; top: 88px; width: 164px; height: 176px; background: var(--paper); padding: 7px; }
  .house-photo {
    width: 100%; height: 100%;
    background: linear-gradient(180deg, #cfe0ee 0%, #e3e8ec 18%, #9a8f86 28%, #5f6a72 40%, #57626a 62%, #7a6a5a 70%, #4f7b3a 78%, #6fa050 90%, #5a8140 100%);
  }

  .price-tag { left: 461px; top: 270px; width: 124px; height: 45px; background: var(--brand-red); color: var(--paper); font-family: "Arimo", sans-serif; font-weight: 700; padding: 6px 0 0 9px; }
  .price-tag .label { font-size: 7.5px; letter-spacing: .2px; }
  .price-tag .amount { font-size: 19px; line-height: 1.1; }

  .offer { left: 414px; top: 339px; font-family: "Arimo", sans-serif; font-weight: 700; }
  .offer .earn { color: var(--brand-red); font-size: 12.5px; }
  .offer .call { color: var(--ink); font-size: 10.5px; margin-top: 1px; }
  .offer .phone { color: var(--brand-red); font-size: 16px; margin-top: 1px; }

  /* Inner spread */
  .inner { left: 205px; top: 515px; width: 587px; height: 410px; background: var(--paper); }
  .inner-head { left: 0; top: 0; width: 587px; height: 45px; background: var(--brand-red); }
  .inner-foot { left: 0; top: 310px; width: 587px; height: 100px; background: var(--brand-red); }
  .level-title { top: 9px; color: var(--paper); font-size: 13px; line-height: 1.05; }
  .level-title b { font-weight: 800; display: block; }
  .level-title span { font-weight: 300; display: block; }
  .floor-plan {
    top: 68px; height: 104px; border: 2px solid #c38a52;
    background:
      linear-gradient(90deg, rgba(195,138,82,.25) 1px, transparent 1px) 0 0 / 28px 100%,
      linear-gradient(180deg, rgba(195,138,82,.25) 1px, transparent 1px) 0 0 / 100% 26px,
      #fbfaf8;
  }
  .room-photo { top: 198px; width: 159px; height: 89px; }
  .room-basement { background: linear-gradient(180deg, #efeeec 0%, #d9d5cf 35%, #8a7a66 55%, #5d5750 70%, #a78a6a 85%, #8b7560 100%); }
  .room-main { background: linear-gradient(180deg, #f0efed 0%, #d5d2cd 40%, #7c7874 60%, #4f4d4b 75%, #8a7f73 100%); }
  .room-upper { background: linear-gradient(180deg, #ecebe8 0%, #cfcac3 35%, #bcb6ae 55%, #a48a6a 75%, #8f7a62 100%); }
  .level-copy { top: 324px; width: 160px; color: var(--paper); font-size: 7px; line-height: 1.4; text-align: justify; }
</style>
</head>
<body>
<div class="canvas">

  <section class="outer abs" aria-label="Brochure outer spread">
    <div class="kitchen-photo abs" role="img" aria-label="Kitchen interior with window, island and bar stools"></div>
    <div class="red-top abs"></div>
    <div class="red-side abs"></div>
    <div class="red-foot-left abs"></div>
    <div class="red-foot abs"></div>

    <h2 class="why-title abs">WHY US:</h2>
    <div class="why-box abs" style="left:233px;top:123px">
      <svg class="why-icon" viewBox="0 0 24 24" aria-hidden="true"><path d="M3 11 12 4l9 7"/><path d="M5 10v10h14V10"/><path d="M10 20v-6h4v6"/></svg>
    </div>
    <div class="why-box abs" style="left:307px;top:123px">
      <svg class="why-icon" viewBox="0 0 24 24" aria-hidden="true"><circle cx="12" cy="12" r="9"/><path d="m7.5 12.5 3 3 6-6.5"/></svg>
    </div>
    <div class="why-box abs" style="left:233px;top:198px">
      <svg class="why-icon" viewBox="0 0 24 24" aria-hidden="true"><circle cx="12" cy="12" r="9"/><path d="M12 7v5l3.5 2"/></svg>
    </div>
    <div class="why-box abs" style="left:307px;top:198px">
      <svg class="why-icon" viewBox="0 0 24 24" aria-hidden="true"><path d="M12 3 4 6v6c0 5 3.5 8 8 9 4.5-1 8-4 8-9V6z"/><path d="m8.5 12 2.5 2.5 4.5-5"/></svg>
    </div>
    <div class="why-box abs" style="left:233px;top:273px">
      <svg class="why-icon" viewBox="0 0 24 24" aria-hidden="true"><path d="M12 21s-7-6.5-7-12a7 7 0 0 1 14 0c0 5.5-7 12-7 12z"/><circle cx="12" cy="9" r="2.5"/></svg>
    </div>
    <div class="why-box abs" style="left:307px;top:273px">
      <svg class="why-icon" viewBox="0 0 24 24" aria-hidden="true"><path d="M6 3h3l1.5 4.5-2 1.5a11 11 0 0 0 6.5 6.5l1.5-2L21 15v3a2 2 0 0 1-2 2A16 16 0 0 1 4 5a2 2 0 0 1 2-2z"/></svg>
    </div>

    <div class="brand brand-top abs">
      <span class="brand-mark"></span>
      <span class="brand-name">Northshore<br>Build<br>Co.</span>
    </div>

    <div class="house-frame abs">
      <div class="house-photo" role="img" aria-label="Two-storey custom home exterior with front lawn"></div>
    </div>

    <div class="price-tag abs">
      <div class="label">THIS CAN BE YOUR HOME</div>
      <div class="amount">$ 549 000</div>
    </div>

    <div class="offer abs">
      <div class="earn">Also, earn 1500/m</div>
      <div class="call">Call us and ask how!</div>
      <div class="phone">555 010 2748</div>
    </div>

    <div class="brand brand-foot abs">
      <span class="brand-mark"></span>
      <span class="brand-name">Northshore<br>Build<br>Co.</span>
    </div>
  </section>

  <section class="inner abs" aria-label="Brochure inner spread">
    <div class="inner-head abs"></div>
    <div class="inner-foot abs"></div>

    <h3 class="level-title abs" style="left:17px"><b>BASEMENT</b><span>LEVEL</span></h3>
    <h3 class="level-title abs" style="left:210px"><b>MAIN</b><span>LEVEL</span></h3>
    <h3 class="level-title abs" style="left:414px"><b>UPPER</b><span>FLOOR</span></h3>

    <div class="floor-plan abs" style="left:18px;width:160px" role="img" aria-label="Basement level floor plan"></div>
    <div class="floor-plan abs" style="left:215px;width:160px" role="img" aria-label="Main level floor plan"></div>
    <div class="floor-plan abs" style="left:412px;width:160px" role="img" aria-label="Upper floor plan"></div>

    <div class="room-photo room-basement abs" style="left:19px" role="img" aria-label="Basement kitchen and dining area"></div>
    <div class="room-photo room-main abs" style="left:214px" role="img" aria-label="Main level living room"></div>
    <div class="room-photo room-upper abs" style="left:409px" role="img" aria-label="Upper floor bathroom vanity"></div>

    <p class="level-copy abs" style="left:19px">Fusce sapien sem, feugiat ac nibh vel, ullamcorper dignissim est. Nam auctor lectus id tincidunt ullamcorper. Praesent quis lobortis lectus.<br>Vestibulum at pretium sem, et ullamcorper nibh.</p>
    <p class="level-copy abs" style="left:217px">Proin eu condimentum odio. Praesent et commodo tortor, vel ultricies odio. Nullam rutrum elementum elit quis sodales. Morbi id quam id neque ornare porta.<br>Vestibulum at pretium sem, et ullamcorper nibh.</p>
    <p class="level-copy abs" style="left:409px">Sed hendrerit cursus accumsan. Nulla sapien leo, facilisis non leo sit amet, posuere fringilla neque. Vestibulum at pretium sem, et ullamcorper nibh. Quisque eget orci malesuada, sodales ante nec, finibus lorem.</p>
  </section>

</div>
</body>
</html>
```